***Flyer*** TOLMARDE AUTO TRANSPORT *** Flyer***

I need a flyer design that explain my auto transport business... the design must be eye catching and draws a persons attention at first site. We Tow Cars locally in the City of Houston for a flat rate of $75... We ask that the designer make the $75 standout so it will catch the attention of the reader. Much of the content writing can be gather from my website tolmardeautotransport.example - the designer can use his own images to express his design work... I will attach the logo and some samples of some reason business and post cards designs. If you chose you can also add these images in your designs if it will help.

Size of flyer is 8"x11" front and back

Automotive

Requirements
Must have
• $75 or $75.00
• (555) 274-3186
• service@tolmardeautotransport.example
• www.tolmardeautotransport.example
Nice to have
• WE REALLY WANT TO EARN YOUR BUSINESS
• Note: Please look at my website for content writing to create your flyer.

```html
<!DOCTYPE html>
<html lang="en">
<head>
<meta charset="utf-8">
<title>Tolmarde Auto Transport Flyer</title>
<link href="https://fonts.googleapis.com/css2?family=Montserrat:wght@500;600;700;800&display=swap" rel="stylesheet">
<style>
  :root {
    --metal-light: #d9dbdd;
    --metal-mid: #b4b7ba;
    --metal-dark: #8d9093;
    --red: #b0141b;
    --red-deep: #6e0a0e;
    --red-bright: #d3212a;
    --charcoal: #2f3032;
    --ink: #1d1d1f;
    --white: #ffffff;
  }
  * { margin: 0; padding: 0; box-sizing: border-box; }
  html, body { width: 928px; height: 1200px; overflow: hidden; background: #ffffff; }
  .flyer {
    position: relative;
    width: 928px; height: 1200px;
    overflow: hidden;
    font-family: "Montserrat", Arial, sans-serif;
    color: var(--white);
  }
  .flyer-art { position: absolute; inset: 0; }
  .brand {
    position: absolute; left: 58px; top: 140px;
    display: flex; align-items: center; gap: 14px;
    color: var(--red-deep);
    font-weight: 800;
  }
  .brand-mark { width: 30px; height: 30px; background: var(--red-deep); }
  .brand-name { font-size: 40px; line-height: 1; letter-spacing: 1px; }
  .brand-sub { display: block; font-size: 26px; letter-spacing: 0.5px; margin-top: 6px; }

  .flat-rate {
    position: absolute; left: 58px; top: 236px;
    display: flex; align-items: center; gap: 14px;
    color: var(--red);
  }
  .flat-rate-price { font-size: 72px; font-weight: 800; line-height: 1; letter-spacing: -1px; }
  .flat-rate-label {
    font-size: 15px; font-weight: 700; line-height: 1.25; color: var(--charcoal);
    letter-spacing: 0.5px;
  }

  .service { position: absolute; }
  .service h2 {
    font-size: 14px; font-weight: 600; letter-spacing: 0.4px;
    line-height: 1.2; margin-bottom: 6px;
  }
  .service p { font-size: 10px; font-weight: 700; line-height: 1.55; }
  .service-fast { left: 622px; top: 381px; width: 290px; }
  .service-fast h2 { padding-left: 56px; margin-bottom: 12px; }
  .service-fast h2 .indent { display: block; margin-left: -27px; }
  .service-fast p { font-size: 10px; }
  .service-inoperable { left: 390px; top: 612px; width: 482px; }
  .service-relocation { left: 390px; top: 797px; width: 500px; }

  .footer-intro {
    position: absolute; left: 30px; top: 990px; width: 868px;
    text-align: center; font-size: 12.5px; font-weight: 600; line-height: 1.5;
  }
  .footer-headline {
    position: absolute; left: 0; top: 1028px; width: 928px;
    text-align: center; font-size: 22px; font-weight: 600; letter-spacing: 1px;
  }
  .contact-block { position: absolute; top: 1076px; }
  .contact-block h3 { font-size: 13px; font-weight: 600; letter-spacing: 0.3px; margin-bottom: 3px; }
  .contact-block p { font-size: 10.5px; font-weight: 700; line-height: 1.5; }
  .contact-block .phone-number { font-size: 15px; font-weight: 600; }
  .location { left: 46px; }
  .contact { left: 250px; }
  .hours { position: absolute; left: 523px; top: 1098px; font-size: 10.5px; font-weight: 700; line-height: 1.6; }
</style>
</head>
<body>
<div class="flyer">
  <svg class="flyer-art" width="928" height="1200" viewBox="0 0 928 1200">
    <defs>
      <linearGradient id="metal" x1="0" y1="0" x2="1" y2="0.2">
        <stop offset="0" stop-color="var(--metal-mid)"/>
        <stop offset="0.35" stop-color="var(--metal-light)"/>
        <stop offset="0.65" stop-color="var(--metal-mid)"/>
        <stop offset="1" stop-color="var(--metal-light)"/>
      </linearGradient>
      <linearGradient id="redPanel" x1="0" y1="0" x2="1" y2="0">
        <stop offset="0" stop-color="var(--red-deep)"/>
        <stop offset="0.5" stop-color="var(--red)"/>
        <stop offset="1" stop-color="var(--red-bright)"/>
      </linearGradient>
      <linearGradient id="darkBand" x1="0" y1="0" x2="1" y2="0">
        <stop offset="0" stop-color="#3a3b3d"/>
        <stop offset="0.5" stop-color="#242527"/>
        <stop offset="1" stop-color="#3a3b3d"/>
      </linearGradient>
      <linearGradient id="photoWarm" x1="0" y1="0" x2="1" y2="1">
        <stop offset="0" stop-color="#c9c2b4"/>
        <stop offset="0.6" stop-color="#6f7c93"/>
        <stop offset="1" stop-color="#b3242a"/>
      </linearGradient>
      <linearGradient id="photoRoad" x1="0" y1="0" x2="1" y2="1">
        <stop offset="0" stop-color="#9aa98a"/>
        <stop offset="0.5" stop-color="#d6d8da"/>
        <stop offset="1" stop-color="#5a6f49"/>
      </linearGradient>
      <linearGradient id="photoCurb" x1="0" y1="0" x2="1" y2="1">
        <stop offset="0" stop-color="#4f6a99"/>
        <stop offset="0.5" stop-color="#8fa3c4"/>
        <stop offset="1" stop-color="#9b9ea4"/>
      </linearGradient>
    </defs>

    <rect class="bg-metal" width="928" height="1200" fill="url(#metal)"/>

    <polygon points="0,905 928,170 928,190 0,925" fill="var(--red)" opacity="0.85"/>
    <polygon points="0,930 928,195 928,200 0,935" fill="var(--white)" opacity="0.6"/>
    <polygon points="300,340 720,68 740,68 320,340" fill="var(--red)"/>

    <polygon points="580,371 928,371 928,553 537,553 537,400" fill="url(#redPanel)"/>
    <polygon points="480,598 928,598 928,757 363,757 363,690" fill="url(#redPanel)"/>
    <polygon points="363,765 928,765 928,905 363,905" fill="url(#redPanel)"/>

    <polygon points="478,70 928,70 928,312 478,312" fill="url(#photoWarm)"
      role="img" aria-label="Photo: woman checking the engine under the open hood of a red car"/>
    <polygon points="290,345 537,345 537,595 159,595 159,430" fill="url(#photoRoad)"
      role="img" aria-label="Photo: man on a phone call beside a stalled white car on a roadside"/>
    <polygon points="0,625 363,625 363,880 0,880" fill="url(#photoCurb)"
      role="img" aria-label="Photo: older woman on a phone sitting by a broken-down car with its hood open"/>

    <rect y="954" width="928" height="196" fill="url(#darkBand)"/>
    <rect y="1150" width="928" height="50" fill="url(#metal)"/>
  </svg>

  <div class="brand">
    <span class="brand-mark"></span>
    <span class="brand-name">TOLMARDE<span class="brand-sub">AUTO TRANSPORT</span></span>
  </div>

  <div class="flat-rate">
    <span class="flat-rate-price">$75</span>
    <span class="flat-rate-label">FLAT RATE<br>LOCAL TOWING<br>IN HOUSTON</span>
  </div>

  <section class="service service-fast">
    <h2>YOUR CAR WILL BE MOVED<span class="indent">IN 24 HOURS OR LESS</span></h2>
    <p>We are aware of how important is the time when you are stuck on the road or need a vehicle moved quickly. All of our services are door to door and we are able to pick up and move your vehicle within 24 hours.</p>
  </section>

  <section class="service service-inoperable">
    <h2>INOPERABLE VEHICLE TRANSPORT</h2>
    <p>Whether you have broken down or got an inoperable vehicle, we can help. As long as the car is accessible and all tires are aired up we can get it picked up and moved for you! A very important note is that the car must be accessible and not be obstructed. We like to get to your location and get the vehicle in 20 minutes or less. Inless transport!</p>
  </section>

  <section class="service service-relocation">
    <h2>RESIDENTIAL RELOCATION SERVICES</h2>
    <p>Moving a car should never be a stressful thing. Moving your vehicle within the city of Houston is the only thing we do. Transporting your vehicle and finding a company to do it hassle free and with care and honesty can be a tough task. Each company has different prices, different reviews, different standards. We offer a flat rate for all of our vehicle transportation and take personal care in your vehicle.</p>
  </section>

  <p class="footer-intro">Feel free to talk to our representative at any time you please use our contact form on our website or one of our contact numbers. Let us safely transport your vehicles. You can expect a flat rate and exceptional service with us!</p>
  <h1 class="footer-headline">WE WANT TO EARN YOUR BUSINESS!</h1>

  <div class="contact-block location">
    <h3>OUR LOCATION</h3>
    <p>Tolmarde Auto Transport<br>Houston, Texas</p>
  </div>
  <div class="contact-block contact">
    <h3>CONTACT US</h3>
    <p>Telephone: <span class="phone-number">(555) 274-3186</span><br>E-mail: service@tolmardeautotransport.example</p>
  </div>
  <p class="hours">Open: Mon - Fri: 8:00 AM - 6:00 PM<br>www.tolmardeautotransport.example</p>
</div>
</body>
</html>
```